TerraLume Business Card Design Project

We need a business card design for a new company called "TerraLume Systems". TerraLume provides 3D visualization software for subsurface oil and gas data so you can make confident downhole decisions.

Our goal is to provide easy to understand big pictures of your data so your can make confident planning decisions.

Our tagline is
SEAMLESS DATA SHARING. EFFECTIVE COLLABORATION. CONFIDENT DECISION-MAKING

Check out http://www.terralume-example.com for more ideas.

The design should promote a technology company that delivers web-based solutions focused on photo-realistic 3D graphics.

The colors from our existing logo (attached) are one option but not a requirement. The design SHOULD NOT use the existing logo.

The design should be two sided and full color. If you require any special print considerations (example: paper type, matte finish, metallic ink, etc) please provide detailed comments. Please also specify any desired details such as rounding of corners, etc.

IF YOU USE BLACK our printer states "We recommend using CMYK black (0, 0, 0, 100) or for a rich black (60, 40, 40, 100). Ensure your artwork is in CMYK mode before adjusting the black."

For design purposes you can use the following contact information

name: Harlan Pike
title: founder
phone: 555.987.6543
email: harlan@terralume-example.com

company information
TerraLume is our "branded" name
"TerraLume Systems" is our official name
www.terralume-example.com

address:
Suite 720
482 Birchmont Avenue SW
Calgary, AB, Canada
T3K 4R8

Target Market(s)

Companies spend a lot of time collecting, organizing and analyzing data but it's really hard to to get a big picture view of current and planned projects, especially in context to existing wellbores, geology and downhole equipment

TerraLume enables you to explore the big picture in an immersive, 3D environment. Our goal is to help transform you rich data into an easily understood picture, to make confident planning decisions and anticipate trouble events before the expensive execution phase.

Industry/Entity Type

Oil And Gas

Requirements
Must have
• The business card design should be sized to a standard 3.5 x 2 inches and print ready. See the attachment for a sample sized card
It MUST meet these requirements:
Exported as PDF file with two pages:
page 1: front design
page 2: back design
All Images must be 300ppi or higher (at 100%)
CMYK colour mode
0.125 inches of bleed on all sides (0.25 inches additional width and height)
0.125 inch safety margin (inside trim line)

```html
<!DOCTYPE html>
<html lang="en">
<head>
<meta charset="utf-8">
<title>TerraLume Business Card</title>
<link rel="stylesheet" href="https://fonts.googleapis.com/css2?family=Montserrat:wght@300;400;600;800;900&display=swap">
<style>
  :root {
    --canvas: #b9b9b9;
    --paper: #ffffff;
    --ink: #1e1e1e;
    --green: #7dc242;
    --green-dark: #4f9a25;
    --green-light: #a6dc63;
    --grey-text: #8a8a8a;
    --white-text: #f2f2f2;
  }
  html, body {
    margin: 0;
    padding: 0;
    width: 1200px;
    height: 861px;
    overflow: hidden;
    background: var(--canvas);
    font-family: "Montserrat", Arial, sans-serif;
  }
  .sheet {
    position: relative;
    width: 1200px;
    height: 861px;
  }
  .card {
    position: absolute;
    top: 276px;
    width: 540px;
    height: 309px;
    background: var(--paper);
    box-shadow: 0 6px 18px rgba(0,0,0,0.22);
    overflow: hidden;
  }
  .card--back { left: 40px; }
  .card--front { left: 620px; }
  .card__art {
    position: absolute;
    inset: 0;
    width: 540px;
    height: 309px;
  }
  .brand {
    position: absolute;
    display: flex;
    align-items: center;
    gap: 10px;
    color: var(--green);
    font-weight: 600;
    letter-spacing: -0.5px;
    white-space: nowrap;
  }
  .brand__mark {
    width: 22px;
    height: 22px;
    background: var(--ink);
  }
  .card--back .brand { left: 40px; bottom: 36px; font-size: 30px; }
  .card--front .brand { right: 22px; top: 78px; font-size: 27px; }

  .web {
    position: absolute;
    right: 26px;
    top: 20px;
    color: var(--white-text);
    font-weight: 800;
    font-size: 17px;
    letter-spacing: 0.2px;
    white-space: nowrap;
  }
  .tagline {
    position: absolute;
    right: 26px;
    top: 54px;
    margin: 0;
    text-align: right;
    color: var(--green);
    font-weight: 300;
    font-size: 19px;
    line-height: 1.2;
    text-transform: uppercase;
    white-space: nowrap;
  }
  .tagline span { display: block; }

  .person {
    position: absolute;
    left: 34px;
    top: 70px;
  }
  .person__name {
    margin: 0;
    color: var(--green);
    font-weight: 900;
    font-size: 32px;
    letter-spacing: 1px;
    text-transform: uppercase;
    line-height: 1;
    white-space: nowrap;
  }
  .person__title {
    margin: 6px 0 0;
    color: var(--grey-text);
    font-weight: 800;
    font-size: 21px;
  }
  .contact {
    position: absolute;
    left: 34px;
    top: 160px;
    margin: 0;
    padding: 0;
    list-style: none;
    color: var(--white-text);
    font-size: 12.5px;
    line-height: 1.35;
  }
  .contact li {
    display: flex;
    margin-bottom: 9px;
    white-space: nowrap;
  }
  .contact__key {
    width: 22px;
    color: var(--green);
    font-weight: 800;
  }
</style>
</head>
<body>
<main class="sheet">

  <section class="card card--back" aria-label="Card back">
    <svg class="card__art" viewBox="0 0 540 309" aria-hidden="true">
      <defs>
        <linearGradient id="back-fade" x1="0" y1="0" x2="0.6" y2="1">
          <stop offset="0" stop-color="#dcdcdc"/>
          <stop offset="1" stop-color="#ffffff"/>
        </linearGradient>
        <linearGradient id="back-green" x1="0" y1="0" x2="1" y2="1">
          <stop offset="0" stop-color="var(--green-light)"/>
          <stop offset="1" stop-color="var(--green-dark)"/>
        </linearGradient>
      </defs>
      <rect width="540" height="309" fill="url(#back-fade)" role="img" aria-label="Soft grey fade standing in for a fine grid texture"/>
      <polygon points="200,0 540,0 540,309 340,309 290,190 250,110" fill="var(--ink)"/>
      <polygon points="150,58 205,0 222,0 268,118 300,186 262,150" fill="url(#back-green)"/>
      <polygon points="250,110 300,188 340,309 318,309 272,190" fill="var(--green)"/>
    </svg>
    <div class="web">www.terralume-example.com</div>
    <p class="tagline">
      <span>Seamless data</span>
      <span>sharing</span>
      <span>Effective</span>
      <span>collaboration</span>
      <span>Confident</span>
      <span>decision-making</span>
    </p>
    <div class="brand"><span class="brand__mark"></span>TerraLume</div>
  </section>

  <section class="card card--front" aria-label="Card front">
    <svg class="card__art" viewBox="0 0 540 309" aria-hidden="true">
      <defs>
        <linearGradient id="front-fade" x1="1" y1="0" x2="0.4" y2="1">
          <stop offset="0" stop-color="#dcdcdc"/>
          <stop offset="1" stop-color="#ffffff"/>
        </linearGradient>
        <linearGradient id="front-green" x1="0" y1="0" x2="1" y2="1">
          <stop offset="0" stop-color="var(--green-light)"/>
          <stop offset="1" stop-color="var(--green-dark)"/>
        </linearGradient>
      </defs>
      <rect width="540" height="309" fill="url(#front-fade)" role="img" aria-label="Soft grey fade standing in for a fine grid texture"/>
      <polygon points="0,0 300,0 325,70 370,180 410,309 0,309" fill="var(--ink)"/>
      <polygon points="300,0 325,0 350,65 395,175 432,309 410,309 370,180 325,70" fill="var(--green)"/>
      <polygon points="318,50 360,78 375,140 345,112" fill="url(#front-green)"/>
    </svg>
    <div class="person">
      <h1 class="person__name">Harlan Pike</h1>
      <p class="person__title">Founder</p>
    </div>
    <ul class="contact">
      <li><span class="contact__key">A</span><span>Suite 720, 482 Birchmont Avenue SW<br>Calgary, AB, Canada, T3K 4R8</span></li>
      <li><span class="contact__key">P</span><span>555.987.6543</span></li>
      <li><span class="contact__key">E</span><span>harlan@terralume-example.com</span></li>
      <li><span class="contact__key">W</span><span>www.terralume-example.com</span></li>
    </ul>
    <div class="brand">TerraLume</div>
  </section>

</main>
</body>
</html>
```